Personal Grocery Shopping Webpage Design

We need a home webpage for a local neighborhood grocery delivery website called "Marrowfield Personal Grocery Shopping & Delivery". We would like to use a color scheme of Grape or Purple and Gray. We would like for the website to have a basic menu bar that includes Home/About Us; Grocery Items; How to Order. we would like to include the uploaded text on the home page. we would like for the website to communicate that this is a personal grocery shopping valet service geared toward upscale customers. The Belvane Ashcourt for personal grocery shopping

```html
<!DOCTYPE html>
<html lang="en">
<head>
<meta charset="utf-8">
<title>Marrowfield Delivery</title>
<link href="https://fonts.googleapis.com/css2?family=Montserrat:wght@300;400;600;700&family=Open+Sans:wght@400;600&display=swap" rel="stylesheet">
<style>
:root{
  --grape:#8a0f4f;
  --ink:#2b2b2b;
  --muted:#8a8a8a;
  --light:#f6f6f6;
  --line:#d4d4d4;
  --night:#3d3a4a;
  --black:#0d0d0d;
  --white:#ffffff;
}
*{margin:0;padding:0;box-sizing:border-box}
html,body{width:1200px;height:2335px;overflow:hidden}
body{position:relative;font-family:"Open Sans",sans-serif;color:var(--ink);background:var(--white)}
.abs{position:absolute}
.btn{position:absolute;background:var(--grape);color:var(--white);font-family:"Montserrat",sans-serif;font-size:12px;font-weight:600;display:flex;align-items:center;justify-content:center;gap:6px}
.section-title{position:absolute;font-family:"Montserrat",sans-serif;font-weight:600;font-size:24px;color:var(--ink);text-align:center;transform:translateX(-50%);white-space:nowrap}
.section-title::after{content:"";display:block;width:40px;height:2px;background:var(--grape);margin:14px auto 0}

/* hero */
.hero{left:0;top:0;width:1200px;height:510px;background:linear-gradient(135deg,#6b5546 0%,#a07a5c 35%,#8c5a4a 60%,#5e6b45 100%)}
.hero-shade{left:0;top:0;width:1200px;height:510px;background:rgba(40,25,25,.35)}
.site-header{left:0;top:0;width:1200px;height:70px;background:rgba(255,255,255,.82)}
.brand{left:156px;top:20px;font-family:"Montserrat",sans-serif;font-weight:600;font-size:22px;color:var(--grape)}
.nav{left:459px;top:25px;display:flex;gap:22px;font-family:"Montserrat",sans-serif;font-size:13px;color:#444}
.nav a{color:inherit;text-decoration:none;padding-bottom:6px}
.nav a.active{color:var(--grape);border-bottom:2px solid var(--grape)}
.cart{left:915px;top:20px;width:128px;height:32px}
.hero-copy{left:0;top:200px;width:1200px;text-align:center;font-family:"Montserrat",sans-serif;font-weight:300;font-size:29px;line-height:38px;color:var(--white)}
.hero-copy b{font-weight:700}
.explore{left:535px;top:341px;width:128px;height:30px}

/* about */
.about-photo{left:156px;top:559px;width:431px;height:288px;background:linear-gradient(160deg,#d9d4cc 0%,#b7a58f 45%,#8a5d3c 75%,#c96b3a 100%)}
.about-title{left:853px;top:588px}
.about-text{left:685px;top:646px;width:358px;text-align:center;font-size:12px;line-height:17.5px;color:var(--muted)}
.read-more{left:783px;top:780px;width:127px;height:31px}

/* items */
.items{left:0;top:895px;width:1200px;height:661px;background:var(--light)}
.items-title{left:600px;top:937px}
.tile{position:absolute;width:204px;height:203px;overflow:hidden}
.tile-label{position:absolute;left:0;bottom:0;width:100%;height:34px;background:rgba(60,60,70,.55);color:var(--white);font-family:"Montserrat",sans-serif;font-weight:600;font-size:15px;display:flex;align-items:center;justify-content:center}
.tile-hover{position:absolute;inset:0;background:rgba(70,60,80,.55)}
.tile-hover .frame{position:absolute;left:9px;top:9px;right:9px;bottom:9px;border:1px solid rgba(255,255,255,.7)}
.tile-hover .name{position:absolute;top:50px;width:100%;text-align:center;color:var(--white);font-family:"Montserrat",sans-serif;font-weight:600;font-size:15px}
.tile-hover .rule{position:absolute;top:80px;left:92px;width:20px;height:1px;background:var(--white)}
.tile-hover .order{position:absolute;left:54px;top:116px;width:96px;height:31px;border:1px solid rgba(255,255,255,.8);color:var(--white);font-size:11px;display:flex;align-items:center;justify-content:center}
.view-all{left:552px;top:1478px;width:95px;height:30px}

/* order */
.order-photo-frame{left:156px;top:1604px;width:384px;height:279px;background:var(--light)}
.order-photo{left:164px;top:1612px;width:370px;height:265px;border:2px solid var(--grape);background:linear-gradient(135deg,#f3f0f1 0%,#f1c6dc 40%,#7d8fae 70%,#f3f0f1 100%)}
.order-title{left:853px;top:1636px}
.field{position:absolute;width:179px;height:31px;border:1px solid var(--line);background:var(--white);font-size:10px;color:#555;display:flex;align-items:center;justify-content:space-between;padding:0 8px}
.submit{left:804px;top:1816px;width:97px;height:31px}

/* contact */
.contact{left:0;top:1934px;width:1200px;height:353px;background:var(--night)}
.contact-title{left:600px;top:1974px;color:var(--white)}
.contact-title::after{background:var(--white)}
.info{position:absolute;left:156px;color:var(--white)}
.info h4{font-family:"Montserrat",sans-serif;font-weight:600;font-size:15px;margin-left:26px}
.info p{font-size:12px;line-height:18px;margin:6px 0 0 26px}
.info svg{position:absolute;left:0;top:1px}
.input{position:absolute;border:1px solid #c9c6d2;color:var(--white);font-size:11px;padding:8px 10px}
.send{left:460px;top:2206px;width:127px;height:30px}

/* footer */
.footer{left:0;top:2287px;width:1200px;height:48px;background:var(--black);color:var(--white)}
.copyright{left:156px;top:16px;font-size:12px}
.social{right:156px;top:17px;display:flex;gap:20px}
.social span{width:13px;height:13px;border-radius:50%;background:var(--white)}
.social span.alt{background:var(--grape)}
</style>
</head>
<body>

<div class="abs hero" role="img" aria-label="Overhead photo of fresh groceries on a wooden table: vegetables, eggs, meat, flowers and jars"></div>
<div class="abs hero-shade"></div>

<header class="abs site-header">
  <div class="abs brand">Marrowfield Delivery</div>
  <nav class="abs nav">
    <a class="active" href="#">Home</a>
    <a href="#">About Us</a>
    <a href="#">Grocery Items</a>
    <a href="#">How to Order</a>
    <a href="#">Contact Us</a>
  </nav>
  <div class="btn cart">
    <svg width="13" height="12" viewBox="0 0 13 12"><path d="M0 1h2l2 7h7l2-5H4" fill="none" stroke="#fff" stroke-width="1.5"/><circle cx="5" cy="10.5" r="1.2" fill="#fff"/><circle cx="10" cy="10.5" r="1.2" fill="#fff"/></svg>
    Item $0.00
  </div>
</header>

<div class="abs hero-copy">Our company will also <b>delivery</b><br>your full list of <b>grocery items</b> within<br><b>90 minutes</b> or less.</div>
<div class="btn explore">Explore More</div>

<div class="abs about-photo" role="img" aria-label="Kitchen counter full of fresh produce, bread, eggs and flowers"></div>
<h2 class="section-title about-title">About Us</h2>
<p class="abs about-text">There are many variations of passages of Lorem Ipsum available, but the majority have suffered alteration in some form, by injected humour, or randomised words which don't look even slightly believable. If you are going to use a passage of Lorem Ipsum, you need to be sure there isn't anything embarrassing hidden in the...</p>
<div class="btn read-more">Read More</div>

<section class="abs items"></section>
<h2 class="section-title items-title">Convenience Store Items</h2>

<div class="tile" style="left:156px;top:1013px;background:linear-gradient(135deg,#7a5a3a,#3a1a1e 55%,#6d4c5a)" role="img" aria-label="Glass of red wine with grapes"><div class="tile-label">Wine</div></div>
<div class="tile" style="left:384px;top:1013px;background:linear-gradient(135deg,#b3717d,#6a5a6a)" role="img" aria-label="Glasses of soda">
  <div class="tile-hover"><div class="frame"></div><div class="name">Soda</div><div class="rule"></div><div class="order">Order Now</div></div>
</div>
<div class="tile" style="left:612px;top:1013px;background:linear-gradient(135deg,#e8d8b8,#c98a2a 55%,#6a4a2a)" role="img" aria-label="Cup of tea with lemon"><div class="tile-label">Tea</div></div>
<div class="tile" style="left:840px;top:1013px;background:linear-gradient(135deg,#dfe6ee,#f4f1e4 50%,#e9c65a)" role="img" aria-label="Jug of milk and cheese"><div class="tile-label">Milk</div></div>
<div class="tile" style="left:156px;top:1240px;background:linear-gradient(135deg,#6b5a3a,#d8782a 50%,#7a2a2a)" role="img" aria-label="Assorted groceries and produce"><div class="tile-label">Grocery</div></div>
<div class="tile" style="left:384px;top:1240px;background:linear-gradient(135deg,#e8e8e2,#d9d42a 45%,#5fae4a)" role="img" aria-label="Cleaning bucket, gloves and spray bottles"><div class="tile-label">Cleaning</div></div>
<div class="tile" style="left:612px;top:1240px;background:linear-gradient(135deg,#b8b4ad,#c9a04a 45%,#eae8e4)" role="img" aria-label="Beauty oils and a potted plant"><div class="tile-label">Health &amp; Beauty</div></div>
<div class="tile" style="left:840px;top:1240px;background:linear-gradient(135deg,#7a5a3a,#3a1a1e 55%,#6d4c5a)" role="img" aria-label="Glass of red wine with grapes"><div class="tile-label">Wine</div></div>

<div class="btn view-all">View All</div>

<div class="abs order-photo-frame"></div>
<div class="abs order-photo" role="img" aria-label="Shopper pushing a cart full of groceries"></div>
<svg class="abs" style="left:568px;top:1604px" width="74" height="280" viewBox="0 0 74 280"><path d="M4 2 C40 2 40 20 40 60 L40 118 C40 132 52 140 70 140 C52 140 40 148 40 162 L40 220 C40 260 40 278 4 278" fill="none" stroke="#f0f0f0" stroke-width="6"/></svg>
<h2 class="section-title order-title">How To Order?</h2>
<div class="field" style="left:663px;top:1712px">Grocery Items<span>›</span></div>
<div class="field" style="left:865px;top:1712px">Size<span>›</span></div>
<div class="field" style="left:663px;top:1758px">Brand<span>›</span></div>
<div class="field" style="left:865px;top:1758px">Flavor<span>›</span></div>
<div class="btn submit">Submit</div>

<section class="abs contact"></section>
<h2 class="section-title contact-title">Contact Us</h2>

<div class="info" style="top:2052px">
  <svg width="14" height="18" viewBox="0 0 14 18"><path d="M7 0a7 7 0 0 0-7 7c0 5 7 11 7 11s7-6 7-11a7 7 0 0 0-7-7z" fill="#fff"/><circle cx="7" cy="7" r="2.5" fill="#3d3a4a"/></svg>
  <h4>Address :</h4>
  <p>Sed ut perspiciatis unde omnis iste<br>commodi consequatur 123450</p>
</div>
<div class="info" style="top:2134px">
  <svg width="16" height="16" viewBox="0 0 16 16"><path d="M3 1l3 3-2 2c1 2 4 5 6 6l2-2 3 3-2 2C7 15 1 9 1 3z" fill="#fff"/></svg>
  <h4>Phone :</h4>
  <p>555-014-2290</p>
</div>
<div class="info" style="top:2198px">
  <svg width="16" height="12" viewBox="0 0 16 12" style="top:3px"><rect width="16" height="12" fill="#fff"/><path d="M0 0l8 6 8-6" fill="none" stroke="#3d3a4a" stroke-width="1.5"/></svg>
  <h4>Email :</h4>
  <p style="text-decoration:underline">orders@marrowfielddelivery.com</p>
</div>

<div class="input" style="left:460px;top:2054px;width:279px;height:31px">Name :</div>
<div class="input" style="left:762px;top:2054px;width:281px;height:31px">Email :</div>
<div class="input" style="left:460px;top:2101px;width:583px;height:85px">Message :</div>
<div class="btn send">
  <svg width="12" height="12" viewBox="0 0 12 12"><path d="M0 5l12-5-4 12-2-5z" fill="#fff"/></svg>
  Send
</div>

<footer class="abs footer">
  <div class="abs copyright">Copyright © 2016. Marrowfield Delivery.</div>
  <div class="abs social"><span></span><span class="alt"></span><span></span><span></span></div>
</footer>

</body>
</html>
```